Design a Website Mockup for educational online magazine for children

Dear Freelance designers,

We are a child-focused charity looking for a creative design for an educational online magazine for children that will learn about other cultures by watching videos, photos and reading other media created by children from all around the world.

Some of the requirements:

- Target audience is children 10-12 years of age from different countries
- Online magazine will be built using open source Drupal CMS (examples of Drupal magazines include: http://www.quarterlyledger.net/ or you can view more examples at http://www.sitegallerypro.net/categories-listing/Magazines%20%26%20Journals )
- We like clean and uncluttered designs
- We like large buttons and call to action areas
- We like a design that looks playful and almost handmade
- Vivid, bright colours (making strong use of one or more of Sunvale’s primary or secondary colours). Colours will also have to adhere to accessibility guidelines. primary and secondary colours guidelines can be found here: https://www.filecrate.net/s/qto4mnzaxe7p2h3/Primary%20and%20secondary%20colours.pdf
- Wireframes can be seen here: https://www.filecrate.net/s/rx8ud41q27yhp5w/Online%20Magazine%20-%20wireframes.pdf or also attached

Other available materials:

- Logo of program that you can find here: https://www.filecrate.net/s/3tkaewo815zqn6r/sunvale_logo.png
- Full branding guidelines can be found here: https://www.filecrate.net/s/p7vjeh340x538k1/Branding%20Guidelines.pdf
- You can use photos from (http://www.friendwall.net/sunvalecharity) or from http://sunvalelink.org/explore (you are not allowed to use photos for any other purpose that for this contest)

Your submission should include:
- At least 2 mockups that show 1 or more pages from the online magazine website
- Short explanation of your approach to the brief.
- If you can, please provide a mockup of how homepage would look on mobile

Winning entry will be selected based on:

- Design follows the requirements explained above
- Design can be implemented using a PHP based content management system like Drupal
- Design follows the wireframe(s) structure
- Design follows branding guidelines

```html
<!DOCTYPE html>
<html lang="en">
<head>
<meta charset="utf-8">
<title>Sunvale Connect – Online Magazine</title>
<link rel="stylesheet" href="https://fonts.googleapis.com/css2?family=Mulish:wght@400;600;800&family=Questrial&family=Arimo:ital,wght@0,400;0,700;1,400&display=swap">
<style>
:root{
  --sky-top:#5fbdea;
  --sky-bottom:#cdeefb;
  --green:#a6c22a;
  --green-dark:#7f9c14;
  --green-deep:#5f7a0c;
  --orange:#f58220;
  --blue:#1c98d6;
  --star:#f3b312;
  --ink:#4a4a4a;
  --ink-soft:#8a8a8a;
  --rule:#e2e2e2;
  --page:#f1f1ee;
  --panel:#ffffff;
  --white:#ffffff;
}
*{box-sizing:border-box;margin:0;padding:0}
html,body{width:1200px;height:1200px;overflow:hidden}
body{position:relative;background:var(--page);font-family:"Arimo",Arial,sans-serif;color:var(--ink)}
.abs{position:absolute}

/* Header */
.header{left:0;top:0;width:1200px;height:150px;background:linear-gradient(180deg,var(--sky-top),var(--sky-bottom))}
.brand{left:247px;top:32px;display:flex;align-items:center;gap:8px}
.brand-dot{width:22px;height:22px;border-radius:50%;background:var(--green)}
.brand-name{font-family:"Mulish",sans-serif;font-weight:800;font-size:25px;color:var(--green-deep)}
.cover-stack{left:513px;top:12px;width:168px;height:62px;border-radius:3px;background:linear-gradient(90deg,#8aa6b8,#f2c53a 45%,#e07b2f)}
.cover-caption{left:513px;top:76px;width:168px;text-align:center;font-family:"Questrial",sans-serif;font-size:14px;color:#5a6a74}
.languages{left:737px;top:0;width:124px;height:14px;background:var(--green);color:var(--white);font-size:8px;font-weight:700;display:flex;align-items:center;justify-content:center;gap:4px;clip-path:polygon(0 0,100% 0,92% 100%,8% 100%)}
.languages i{width:7px;height:7px;border-radius:50%;background:var(--white);display:inline-block}

.nav{left:251px;top:91px;width:673px;height:52px;background:var(--white);border:1px solid var(--rule);display:flex;align-items:center;justify-content:space-around;padding:0 12px}
.nav-item{display:flex;align-items:center;gap:8px;font-family:"Questrial",sans-serif;font-size:16px;color:#7a7a7a}
.nav-item.is-active{color:var(--green-dark)}
.nav-item svg{width:36px;height:30px}

/* Hero */
.hero{left:0;top:149px;width:1200px;height:222px;background:linear-gradient(180deg,#b6cf46,var(--green))}
.hero-title{left:243px;top:172px;font-family:"Mulish",sans-serif;font-weight:400;color:var(--white);font-size:29px;line-height:36px}
.hero-title b{font-weight:800}
.hero-title .big{font-size:33px}
.hero-rule{left:243px;top:288px;width:330px;height:1px;background:rgba(255,255,255,.5)}
.hero-text{left:247px;top:294px;width:310px;font-size:10px;font-weight:700;line-height:15px;color:var(--white)}
.hero-photo{left:580px;top:207px;width:380px;height:164px;background:linear-gradient(90deg,#d8a47c,#6da6cf 50%,#8fbf5a);border-radius:4px 4px 0 0}
.hero-dots{left:880px;top:351px;display:flex;gap:4px}
.hero-dots i{width:9px;height:9px;background:#3b8fcf;display:block}
.hero-dots i:first-child{background:var(--white)}
.slide-arrow{top:233px;width:24px;height:24px;background:var(--white);display:flex;align-items:center;justify-content:center}
.slide-arrow.prev{left:0}
.slide-arrow.next{left:1176px}

/* Content panel */
.content{left:261px;top:371px;width:699px;height:617px;background:var(--panel)}
.section-title{font-family:"Questrial",sans-serif;font-size:16px;letter-spacing:.3px;color:#444}
.section-rule{height:1px;background:var(--rule)}
.pager{display:flex;gap:3px}
.pager i{width:11px;height:11px;border-radius:2px;background:#e6e6e6;display:flex;align-items:center;justify-content:center}

.card-row{display:flex;gap:13px}
.card{width:131px;border:1px solid var(--rule);background:var(--white)}
.card-media{display:block}
.card-title{color:var(--white);font-size:9px;padding:0 5px;display:flex;align-items:center}
.card-title.video{background:var(--orange);height:17px}
.card-title.photo{background:var(--blue);height:19px}
.card-meta{font-size:7.5px;color:var(--ink-soft);text-align:center;padding:7px 0 6px;border-bottom:1px solid #eee}
.card-meta span{padding:0 6px}
.card-rating{display:flex;justify-content:space-between;align-items:center;padding:6px 10px 7px 10px;font-size:8px;color:var(--ink-soft)}
.stars{color:var(--star);font-size:12px;letter-spacing:1px}
.stars em{color:#cfcfcf;font-style:normal}

.fact-text{left:270px;top:848px;width:416px;font-size:8.6px;line-height:12.4px;color:#555}
.fact-text p{margin-bottom:5px}

/* Sidebar */
.search{left:733px;top:397px;width:214px;height:24px;display:flex}
.search-field{flex:1;border:1px solid var(--rule);background:var(--white);font-size:9px;color:#bbb;padding:6px}
.search-btn{width:33px;background:var(--green);display:flex;align-items:center;justify-content:center}
.mag-visual{left:731px;top:433px;width:206px;height:143px;background:linear-gradient(90deg,#9bb1c3,#f4cd3a 45%,#dc7a2c);border-radius:3px}
.cta{left:737px;top:580px;width:200px;height:29px;background:var(--orange);display:flex;align-items:center;color:var(--white);font-size:8.5px;font-weight:700;white-space:nowrap}
.cta-icon{width:29px;height:29px;background:var(--blue);display:flex;align-items:center;justify-content:center;margin-right:7px}
.poll-title{left:741px;top:622px;font-family:"Questrial",sans-serif;font-size:17px;color:#444}
.poll-rule{left:741px;top:648px;width:200px}
.poll-q{left:743px;top:657px;font-size:9.5px;color:#444}
.poll-list{left:745px;top:677px;list-style:none}
.poll-list li{font-size:7.5px;color:#555;height:15px;display:flex;align-items:center;gap:8px}
.poll-list li i{width:7px;height:7px;border-radius:50%;border:1px solid #ccc;display:block}
.poll-results{left:746px;top:775px;font-size:9.5px;color:var(--ink-soft)}
.poll-submit{left:895px;top:770px;width:47px;height:19px;background:var(--blue);color:var(--white);font-size:8px;font-weight:700;display:flex;align-items:center;justify-content:center}
.tips-title{left:746px;top:808px;font-family:"Questrial",sans-serif;font-size:17px;color:#555}
.tips-rule{left:743px;top:834px;width:200px}
.tips-list{left:744px;top:840px;list-style:none;width:200px}
.tips-list li{display:flex;gap:10px;height:33px;align-items:flex-start;padding-top:3px;border-bottom:1px solid #efefef;font-size:7.2px;line-height:10.5px;color:#777}
.tips-list svg{flex:none}

/* Footer */
.footer{left:0;top:988px;width:1200px;height:212px;background:var(--green)}
.footer-title{font-family:"Questrial",sans-serif;font-size:18px;color:var(--white)}
.link-list{left:274px;top:1030px;list-style:none}
.link-list li{display:flex;align-items:center;gap:6px;height:13.2px;font-size:8.4px;color:var(--white)}
.about-photo{left:413px;top:1033px;width:72px;height:63px;background:linear-gradient(180deg,#8fb6d6,#3b8a3b);border:2px solid var(--white)}
.about-text{font-size:8px;line-height:13.5px;color:var(--white)}
.about-text em{font-style:italic}
.addr-title{left:762px;top:1034px;font-size:10px;font-weight:700;color:var(--white)}
.addr{left:764px;top:1049px;font-size:6.8px;color:var(--white)}
.pin{left:752px;top:1064px}
.contact-rows{left:800px;top:1064px;list-style:none}
.contact-rows li{display:flex;align-items:center;height:14px;font-size:6.8px;color:var(--white);gap:8px}
.contact-rows li span{width:42px}
.copy{left:798px;top:1108px;font-size:6.8px;color:var(--white)}
.social{left:800px;top:1120px;display:flex;gap:3px}
.social i{width:13px;height:13px;background:var(--white);display:block}
</style>
</head>
<body>

<!-- Header -->
<header class="abs header"></header>
<div class="abs brand"><span class="brand-dot"></span><span class="brand-name">Sunvale Connect</span></div>
<div class="abs cover-stack" role="img" aria-label="Stack of printed magazine covers"></div>
<div class="abs cover-caption">Magzine Name here</div>
<div class="abs languages">LANGUAGES <i></i><i></i><i></i></div>

<svg class="abs" width="820" height="60" viewBox="0 0 820 60" style="left:180px;top:90px">
  <polygon points="0,4 80,4 80,46 0,46 22,25" fill="#ffffff"/>
  <polygon points="820,4 740,4 740,46 820,46 798,25" fill="#ffffff"/>
</svg>
<nav class="abs nav">
  <a class="nav-item is-active">
    <svg viewBox="0 0 36 30"><path d="M4 15 L18 3 L32 15 L28 15 L28 28 L21 28 L21 19 L15 19 L15 28 L8 28 L8 15 Z" fill="#8fb21d"/></svg>Home</a>
  <a class="nav-item">
    <svg viewBox="0 0 36 30"><circle cx="11" cy="8" r="5" fill="#666"/><circle cx="22" cy="8" r="5" fill="#666"/><rect x="4" y="13" width="22" height="13" rx="2" fill="#666"/><polygon points="26,16 34,12 34,27 26,23" fill="#666"/></svg>Video</a>
  <a class="nav-item">
    <svg viewBox="0 0 36 30"><rect x="3" y="8" width="30" height="20" rx="2" fill="#666"/><rect x="10" y="4" width="10" height="5" fill="#666"/><circle cx="18" cy="18" r="6" fill="#fff"/><circle cx="18" cy="18" r="3.5" fill="#666"/></svg>Photos</a>
  <a class="nav-item">
    <svg viewBox="0 0 36 30"><path d="M3 6 Q11 3 18 8 Q25 3 33 6 L33 26 Q25 23 18 27 Q11 23 3 26 Z" fill="#666"/><path d="M18 8 L18 27" stroke="#fff" stroke-width="1.5"/><path d="M7 12 H14 M7 16 H14 M22 12 H29 M22 16 H29" stroke="#fff" stroke-width="1.2"/></svg>Creative</a>
  <a class="nav-item">
    <svg viewBox="0 0 36 30"><circle cx="18" cy="15" r="13" fill="#666"/><path d="M10 9 Q15 7 17 11 Q14 16 10 14 Z M20 18 Q26 15 27 21 Q23 25 20 23 Z" fill="#fff"/></svg>Where</a>
</nav>

<!-- Hero -->
<section class="abs hero"></section>
<h1 class="abs hero-title">One <b>Child</b>,one <b>teacher</b>,<br>one book and one <b>pen</b><br>can change the <b class="big">world</b>"</h1>
<div class="abs hero-rule"></div>
<p class="abs hero-text">We have wonderful Friday news to share with you! Sunvale has been selected as one of 10 finalists for a global award</p>
<div class="abs hero-photo" role="img" aria-label="Group of smiling schoolchildren standing together"></div>
<div class="abs hero-dots"><i></i><i></i><i></i><i></i></div>
<div class="abs slide-arrow prev"><svg width="10" height="12"><polygon points="9,0 9,12 1,6" fill="#7f9c14"/></svg></div>
<div class="abs slide-arrow next"><svg width="10" height="12"><polygon points="1,0 1,12 9,6" fill="#7f9c14"/></svg></div>

<!-- Main content -->
<main class="abs content"></main>

<h2 class="abs section-title" style="left:270px;top:392px">LATEST VIDEOS</h2>
<div class="abs pager" style="left:663px;top:396px"><i></i><i></i></div>
<div class="abs section-rule" style="left:268px;top:414px;width:421px"></div>
<div class="abs card-row" style="left:268px;top:431px">
  <article class="card"><div class="card-media" role="img" aria-label="Video still of a child" style="height:86px;background:linear-gradient(135deg,#c9a58a,#6d6f8a)"></div><div class="card-title video">Title of video</div><div class="card-meta"><span>Australia</span>|<span>Edition</span>|<span>2013</span></div><div class="card-rating"><span class="stars">★★★★<em>★</em></span>Rating</div></article>
  <article class="card"><div class="card-media" role="img" aria-label="Video still of children outdoors" style="height:86px;background:linear-gradient(135deg,#9fc37a,#3c7a3e)"></div><div class="card-title video">Title of video</div><div class="card-meta"><span>Australia</span>|<span>Edition</span>|<span>2013</span></div><div class="card-rating"><span class="stars">★★★★<em>★</em></span>Rating</div></article>
  <article class="card"><div class="card-media" role="img" aria-label="Video still of a group in green shirts" style="height:86px;background:linear-gradient(135deg,#4f9a4a,#b88a6a)"></div><div class="card-title video">Title of video</div><div class="card-meta"><span>Australia</span>|<span>Edition</span>|<span>2013</span></div><div class="card-rating"><span class="stars">★★★★<em>★</em></span>Rating</div></article>
</div>

<h2 class="abs section-title" style="left:266px;top:604px">LATEST PHOTOSTORIES</h2>
<div class="abs pager" style="left:661px;top:609px"><i></i><i></i></div>
<div class="abs section-rule" style="left:266px;top:628px;width:423px"></div>
<div class="abs card-row" style="left:266px;top:644px">
  <article class="card"><div class="card-media" role="img" aria-label="Photo of volunteers in green shirts" style="height:79px;background:linear-gradient(135deg,#3f8f3c,#c98e6a)"></div><div class="card-title photo">Title of photostories</div><div class="card-meta"><span>Australia</span>|<span>Edition</span>|<span>2013</span></div><div class="card-rating"><span class="stars">★★★★<em>★</em></span>Rating</div></article>
  <article class="card"><div class="card-media" role="img" aria-label="Photo of people gathered outdoors" style="height:79px;background:linear-gradient(135deg,#9ccb6a,#4b7d3b)"></div><div class="card-title photo">Title of photostories</div><div class="card-meta"><span>Australia</span>|<span>Edition</span>|<span>2013</span></div><div class="card-rating"><span class="stars">★★★★<em>★</em></span>Rating</div></article>
  <article class="card"><div class="card-media" role="img" aria-label="Photo of a child with an adult" style="height:79px;background:linear-gradient(135deg,#8fa0b5,#7a5540)"></div><div class="card-title photo">Title of photostories</div><div class="card-meta"><span>Australia</span>|<span>Edition</span>|<span>2013</span></div><div class="card-rating"><span class="stars">★★★★<em>★</em></span>Rating</div></article>
</div>

<h2 class="abs section-title" style="left:270px;top:816px">DID YOU KNOW?</h2>
<div class="abs pager" style="left:659px;top:821px"><i></i><i></i></div>
<div class="abs section-rule" style="left:266px;top:838px;width:423px"></div>
<div class="abs fact-text">
  <p>The World Kids Council' survey for a better world. This year we included it in our annual global children's survey, so kids like 10-year-old Amani and her friends from</p>
  <p>The World Kids Council' survey for a better world. This year we included it in our annual global children's survey, so kids <i>like 10-year-old Amani and her friends from</i> The World Kids Council' survey for a better world. This year we included it in our annual global children's survey, so kids <i>like 10-year-old Amani and her</i><br>The World Kids Council' survey for a better world. This year we included it in our annual global children's survey, so kids like 10-year-old Amani and her friends from The World Kids Council' survey.</p>
</div>
<div class="abs section-rule" style="left:266px;top:955px;width:423px"></div>

<!-- Sidebar -->
<div class="abs search"><div class="search-field">Search Text here</div><div class="search-btn"><svg width="16" height="16"><circle cx="6.5" cy="6.5" r="4.5" stroke="#fff" stroke-width="2.2" fill="none"/><line x1="10" y1="10" x2="15" y2="15" stroke="#fff" stroke-width="2.6"/></svg></div></div>
<div class="abs mag-visual" role="img" aria-label="Fanned stack of printed magazine issues"></div>
<a class="abs cta"><span class="cta-icon"><svg width="14" height="16"><rect x="5" y="0" width="4" height="8" fill="#fff"/><polygon points="0,7 14,7 7,15" fill="#fff"/></svg></span>Download our Latest printed magazine</a>
<h3 class="abs poll-title">Poll</h3>
<div class="abs section-rule poll-rule"></div>
<p class="abs poll-q">What do you think about..?</p>
<ul class="abs poll-list">
  <li><i></i>I am very proud to say that</li>
  <li><i></i>We are so thankful to have such</li>
  <li><i></i>I am very proud to say that</li>
  <li><i></i>We are so thankful to have such</li>
  <li><i></i>I am very proud to say that</li>
  <li><i></i>We are so thankful to have such</li>
</ul>
<span class="abs poll-results">Results</span>
<a class="abs poll-submit">SUBMIT</a>

<h3 class="abs tips-title">TIPS &amp; TRICKS</h3>
<div class="abs section-rule tips-rule"></div>
<ul class="abs tips-list">
  <li><svg width="24" height="24"><circle cx="11" cy="13" r="9" stroke="#1c98d6" stroke-width="2" fill="none"/><path d="M6 12 L11 17 L22 4" stroke="#1c98d6" stroke-width="3" fill="none"/></svg><span>PHOTO OF THE WEEK: Today is International Day of the Girl Child, which is celebrated</span></li>
  <li><svg width="24" height="24"><circle cx="11" cy="13" r="9" stroke="#1c98d6" stroke-width="2" fill="none"/><path d="M6 12 L11 17 L22 4" stroke="#1c98d6" stroke-width="3" fill="none"/></svg><span>PHOTO OF THE WEEK: Today is International Day of the Girl Child, which is celebrated</span></li>
  <li><svg width="24" height="24"><circle cx="11" cy="13" r="9" stroke="#1c98d6" stroke-width="2" fill="none"/><path d="M6 12 L11 17 L22 4" stroke="#1c98d6" stroke-width="3" fill="none"/></svg><span>PHOTO OF THE WEEK: Today is International Day of the Girl Child, which is celebrated</span></li>
</ul>
<div class="abs pager" style="left:920px;top:937px"><i></i><i></i></div>

<!-- Footer -->
<footer class="abs footer"></footer>
<h4 class="abs footer-title" style="left:272px;top:1003px">OUR LINKS</h4>
<ul class="abs link-list">
  <li><svg width="9" height="9"><circle cx="4.5" cy="4.5" r="3.8" stroke="#fff" fill="none"/><path d="M2.5 4.5 L4 6 L7 2.5" stroke="#fff" fill="none"/></svg>Home</li>
  <li><svg width="9" height="9"><circle cx="4.5" cy="4.5" r="3.8" stroke="#fff" fill="none"/><path d="M2.5 4.5 L4 6 L7 2.5" stroke="#fff" fill="none"/></svg>About Sunvale</li>
  <li><svg width="9" height="9"><circle cx="4.5" cy="4.5" r="3.8" stroke="#fff" fill="none"/><path d="M2.5 4.5 L4 6 L7 2.5" stroke="#fff" fill="none"/></svg>Video</li>
  <li><svg width="9" height="9"><circle cx="4.5" cy="4.5" r="3.8" stroke="#fff" fill="none"/><path d="M2.5 4.5 L4 6 L7 2.5" stroke="#fff" fill="none"/></svg>Photos</li>
  <li><svg width="9" height="9"><circle cx="4.5" cy="4.5" r="3.8" stroke="#fff" fill="none"/><path d="M2.5 4.5 L4 6 L7 2.5" stroke="#fff" fill="none"/></svg>Creative</li>
  <li><svg width="9" height="9"><circle cx="4.5" cy="4.5" r="3.8" stroke="#fff" fill="none"/><path d="M2.5 4.5 L4 6 L7 2.5" stroke="#fff" fill="none"/></svg>Where</li>
  <li><svg width="9" height="9"><circle cx="4.5" cy="4.5" r="3.8" stroke="#fff" fill="none"/><path d="M2.5 4.5 L4 6 L7 2.5" stroke="#fff" fill="none"/></svg>Privacy Policy</li>
  <li><svg width="9" height="9"><circle cx="4.5" cy="4.5" r="3.8" stroke="#fff" fill="none"/><path d="M2.5 4.5 L4 6 L7 2.5" stroke="#fff" fill="none"/></svg>Contact Us</li>
</ul>

<h4 class="abs footer-title" style="left:413px;top:1003px">ABOUT SUNVALE</h4>
<div class="abs about-photo" role="img" aria-label="Group photo of the team in green shirts"></div>
<p class="abs about-text" style="left:494px;top:1031px;width:225px">The World Kids Council' survey for a better world. This year we included it in our annual global children's survey, so kids <em>like 10-year-old Amani and her friends from</em><br>The World Kids Council' survey for a better world. This year we included it in our global survey, so kids</p>
<p class="abs about-text" style="left:413px;top:1114px;width:310px">This year we included it in our annual global children's survey, so kids <em>like 10-year-old Amani and her friends from</em></p>

<h4 class="abs footer-title" style="left:758px;top:1003px">CONTACT US</h4>
<p class="abs addr-title">OUR ADDRESS</p>
<p class="abs addr">120 N BRIGHTWATER WAY MARLOW UT 84990</p>
<svg class="abs pin" width="42" height="72">
  <path d="M20 3 C9 3 3 11 3 20 C3 32 20 50 20 50 C20 50 37 32 37 20 C37 11 31 3 20 3 Z" fill="none" stroke="#fff" stroke-width="3"/>
  <circle cx="20" cy="20" r="6" fill="#fff"/>
  <ellipse cx="20" cy="60" rx="15" ry="5" fill="none" stroke="#fff" stroke-width="2.5"/>
</svg>
<ul class="abs contact-rows">
  <li><svg width="10" height="10"><path d="M2 1 L4 1 L5 3.5 L3.8 4.6 Q5 6.8 6.4 7.3 L7.5 6 L10 7 L10 9 Q5 10 1 4 Z" fill="#fff"/></svg><span>TOLL FREE</span>800-555-0142</li>
  <li><svg width="10" height="10"><rect x="2" y="0" width="6" height="10" rx="1" fill="#fff"/></svg><span>PHONE</span>435-555-0187</li>
  <li><svg width="10" height="10"><rect x="0" y="3" width="10" height="5" fill="#fff"/><rect x="2" y="0" width="6" height="3" fill="#fff"/></svg><span>FAX</span>435-555-0193</li>
</ul>
<p class="abs copy">© 2013 sunvale.org</p>
<div class="abs social"><i></i><i></i></div>

</body>
</html>
```